Create the ONLY Supplement line for Male Entrepreneurs! (Verdant Crest MD)

I need a label designed for a new supplement brand that I am launching.

There are five products so need a design that I can simply change the wording for each individual product

The brand name is called verdant crest MD. The focus is male entrepreneurial health.

Target audience is men 35 to 55.

Concepts: the healthier you are in body the more money you will make in business.

Concept to copy: I want to make a clean minimalistic label mimicking Halvorsen MD (google it and you'll see what I mean)
Updates

Target Market(s)

male entrepreneurs 35-55

Industry/Entity Type

Health Supplement

Colors

Designer to choose colors to be used in the design.

Requirements
Must have
• Modern classy design, similar to Halvorsen MD.
Nice to have
• Highlight that the supplement is Doctor Approved.
Should not have
• No loud colors. Present it as high class.

```html
<!DOCTYPE html>
<html lang="en">
<head>
<meta charset="UTF-8">
<title>Verdant Crest MD – Omega 3 Label</title>
<link rel="stylesheet" href="https://fonts.googleapis.com/css2?family=Barlow+Condensed:wght@200&family=Barlow+Semi+Condensed:wght@200;300;400&family=Libre+Franklin:wght@400;600;800;900&display=swap">
<style>
  :root {
    --stage: #e6e7e8;
    --paper: #ffffff;
    --ink: #3a3a3c;
    --ink-text: #2b2b2d;
    --nf-ink: #1d1d1f;
  }
  * { margin: 0; padding: 0; box-sizing: border-box; }
  html, body {
    width: 1200px; height: 658px; overflow: hidden;
    background: var(--stage);
  }
  body { position: relative; }
  .label {
    position: absolute; left: 66px; top: 15px;
    width: 1068px; height: 628px;
    overflow: hidden;
    background: var(--paper);
    box-shadow: 0 2px 8px rgba(0,0,0,0.18);
    font-family: "Barlow Semi Condensed", sans-serif;
    color: var(--ink-text);
  }
  .brand-banner { position: absolute; left: 367px; top: 0; width: 334px; height: 220px; }
  .brand-banner svg { position: absolute; inset: 0; }
  .brand-name {
    position: absolute; left: 0; right: 0; top: 78px;
    text-align: center; font-weight: 300; font-size: 45px; line-height: 54px;
    color: #fff; letter-spacing: 0.5px; white-space: nowrap;
  }
  .brand-rule { position: absolute; left: 30px; right: 32px; top: 136px; height: 1.5px; background: #fff; }
  .brand-sub {
    position: absolute; left: 0; right: 0; top: 145px;
    text-align: center; font-weight: 300; font-size: 28px; line-height: 34px;
    color: #fff; letter-spacing: 0.5px; white-space: nowrap;
  }
  .description {
    position: absolute; left: 52px; top: 130px; width: 235px;
    font-weight: 300; font-size: 17.5px; line-height: 20.5px; text-align: justify;
  }
  .description p + p { margin-top: 20px; }
  .code-panel { position: absolute; left: 52px; top: 438px; width: 161px; height: 79px; background: var(--ink); }
  .approval-mark {
    position: absolute; left: 220px; top: 446px; width: 75px; height: 63px;
    background: var(--ink); border-radius: 4px;
  }
  .product { position: absolute; left: 406px; top: 390px; width: 255px; text-align: center; white-space: nowrap; }
  .product-name {
    font-family: "Barlow Condensed", sans-serif;
    font-weight: 200; font-size: 84px; line-height: 88px; letter-spacing: 1px;
  }
  .potency {
    margin-top: 6px; border-top: 2px solid var(--ink-text); border-bottom: 2px solid var(--ink-text);
    font-weight: 300; font-size: 31px; line-height: 39px; letter-spacing: 4px;
  }
  .volume { margin-top: 6px; font-weight: 300; font-size: 31px; line-height: 36px; }

  .nutrition {
    position: absolute; left: 800px; top: 131px; width: 216px; height: 388px;
    border: 1px solid var(--nf-ink); padding: 2px 4px;
    font-family: "Libre Franklin", sans-serif; color: var(--nf-ink); font-size: 9.5px; line-height: 15.2px;
  }
  .nf-title { font-weight: 900; font-size: 26px; line-height: 28px; letter-spacing: -0.4px; border-bottom: 1px solid var(--nf-ink); white-space: nowrap; }
  .nf-row { display: flex; justify-content: space-between; white-space: nowrap; }
  .nf-servings { font-size: 11px; line-height: 13px; margin-top: 2px; }
  .nf-size { font-weight: 800; font-size: 12px; line-height: 14px; border-bottom: 7px solid var(--nf-ink); padding-bottom: 2px; }
  .nf-small { font-weight: 800; font-size: 7px; line-height: 9px; margin-top: 4px; }
  .nf-calories { font-weight: 900; font-size: 20px; line-height: 22px; border-bottom: 4px solid var(--nf-ink); }
  .nf-calories span:last-child { font-size: 25px; }
  .nf-dv { text-align: right; font-weight: 600; font-size: 7px; line-height: 14px; border-bottom: 1px solid var(--nf-ink); }
  .nf-line { border-bottom: 1px solid var(--nf-ink); }
  .nf-line b, .nf-line .pct, .nf-protein b { font-weight: 800; }
  .in1 { padding-left: 14px; }
  .in2 { padding-left: 28px; }
  .nf-protein { border-bottom: 7px solid var(--nf-ink); }
  .nf-mineral { font-size: 9.3px; border-bottom: 1px solid var(--nf-ink); }
  .nf-note { font-size: 7.3px; line-height: 9.3px; padding: 2px 0 0 2px; }
</style>
</head>
<body>
  <main class="label">
    <header class="brand-banner">
      <svg width="334" height="220" viewBox="0 0 334 220" aria-hidden="true">
        <polygon points="0,0 334,0 334,184 167,220 0,184" fill="var(--ink)"/>
      </svg>
      <div class="brand-name">verdant crest MD</div>
      <div class="brand-rule"></div>
      <div class="brand-sub">supplement</div>
    </header>

    <section class="description">
      <p>Lorem ipsum dolor sit amet, consectetuer adipiscing elit, sed diam nonummy nibh euismod tincidunt ut laoreet dolore magna aliquam erat volutpat.</p>
      <p>Ut wisi enim ad minim veniam, Lorem ipsum dolor sit amet, consectetuer adipiscing elit, sed diam nonummy nibh euismod tincidunt ut laoreet dolore magna aliquam erat volutpat. Ut wisi enim ad minim veniam.</p>
    </section>

    <div class="code-panel"></div>
    <div class="approval-mark" role="img" aria-label="Doctor approved emblem"></div>

    <section class="product">
      <h1 class="product-name">Omega 3</h1>
      <div class="potency">HIGH POTENCY</div>
      <div class="volume">59 ml / 2fl oz</div>
    </section>

    <aside class="nutrition">
      <div class="nf-title">Nutrition Facts</div>
      <div class="nf-servings">4 servings per container</div>
      <div class="nf-row nf-size"><span>Serving size</span><span>1 cup (180g)</span></div>
      <div class="nf-small">Amount per serving</div>
      <div class="nf-row nf-calories"><span>Calories</span><span>245</span></div>
      <div class="nf-dv">% Daily Value*</div>
      <div class="nf-row nf-line"><span><b>Total Fat</b> 12g</span><span class="pct">14%</span></div>
      <div class="nf-row nf-line in1"><span>Saturated Fat 2g</span><span class="pct">10%</span></div>
      <div class="nf-row nf-line in1"><span><i>Trans</i> Fat 0g</span><span></span></div>
      <div class="nf-row nf-line"><span><b>Cholesterol</b> 8mg</span><span class="pct">3%</span></div>
      <div class="nf-row nf-line"><span><b>Sodium</b> 210mg</span><span class="pct">9%</span></div>
      <div class="nf-row nf-line"><span><b>Total Carbohydrate</b> 34g</span><span class="pct">12%</span></div>
      <div class="nf-row nf-line in1"><span>Dietary Fiber 7g</span><span class="pct">25%</span></div>
      <div class="nf-row nf-line in1"><span>Total Sugars 5g</span><span></span></div>
      <div class="nf-row nf-line in2"><span>Includes 4g Added Sugars</span><span class="pct">8%</span></div>
      <div class="nf-row nf-protein"><span><b>Protein</b> 11g</span><span></span></div>
      <div class="nf-row nf-mineral"><span>Vit. D 4mcg 20%</span><span>·</span><span>Calcium 210mg 16%</span></div>
      <div class="nf-row nf-mineral"><span>Iron 3mg 15%</span><span>·</span><span>Potas. 380mg 8%</span></div>
      <div class="nf-row nf-mineral"><span>Vit. A 84mcg 9%</span><span>·</span><span>Vit. C 10mg 11%</span></div>
      <div class="nf-row nf-mineral"><span>Zinc 7mg 17%</span><span>·</span><span>Iodine 15mcg 10%</span></div>
      <div class="nf-note">*The % Daily Value (DV) tells you how much a nutrient in a serving of food contributes to a daily diet. 2,000 calories a day is used for general nutrition advice.</div>
    </aside>
  </main>
</body>
</html>
```